Flyer-Design für psychologische Beratungspraxis für Mütter
Zielgruppe
Gelassenheitswerkstatt ist eine psychologische Beratungspraxis. Ich unterstütze Mütter, Schwangere und Frauen mit Kinderwunsch bei Herausforderungen rund um Schwangerschaft, Geburt, Mutterschaft, und damit einhergehenden Problemen.
Aufgabenstellung
Text nochmal geringgradig geändert...siehe Datei anbei

```html
<!DOCTYPE html>
<html lang="de">
<head>
<meta charset="utf-8">
<title>Gelassenheitswerkstatt – Flyer</title>
<link rel="stylesheet" href="https://fonts.googleapis.com/css2?family=Roboto:wght@400;700&family=Source+Sans+3:wght@400;700&display=swap">
<style>
  :root {
    --navy: #27307a;
    --navy-deep: #2b3590;
    --green: #3f9f35;
    --accent: #e2552f;
    --cream: #fdfbec;
    --cream-warm: #fbf6d8;
    --page: #eef0ec;
    --white: #ffffff;
  }
  * { margin: 0; padding: 0; box-sizing: border-box; }
  html, body {
    width: 1200px; height: 1200px; overflow: hidden;
    background: var(--page);
  }
  .flyer {
    position: absolute; left: 48px; top: 48px;
    width: 1104px; height: 1104px;
    display: flex;
    box-shadow: 0 4px 18px rgba(0,0,0,0.18);
  }
  .panel { position: relative; width: 552px; height: 100%; overflow: hidden; }
  .panel--contact {
    background: linear-gradient(180deg, var(--cream) 0%, var(--cream-warm) 100%);
    font-family: "Source Sans 3", sans-serif;
    color: var(--navy);
  }
  .panel--cover {
    background: linear-gradient(180deg, var(--cream) 0%, #f4f0d6 45%, #a9a9c6 62%, #6a6fae 80%, var(--navy-deep) 100%);
    font-family: "Roboto", sans-serif;
  }
  .brand {
    position: absolute; left: 0; right: 0; top: 44px;
    display: flex; flex-direction: column; align-items: center; gap: 34px;
  }
  .brand__dot {
    width: 70px; height: 70px; border-radius: 50%;
    background: var(--accent);
  }
  .brand__name {
    font-family: "Source Sans 3", sans-serif;
    font-weight: 700; font-size: 20px; letter-spacing: 1.5px;
    color: var(--navy);
  }
  .centered { position: absolute; left: 0; right: 0; text-align: center; }
  .service { top: 247px; font-size: 20px; letter-spacing: 0.5px; }
  .advisor { top: 288px; font-size: 23px; font-weight: 700; font-family: "Roboto", sans-serif; }
  .credentials { top: 328px; font-size: 19px; line-height: 26px; }
  .portrait {
    position: absolute; left: 128px; top: 402px; width: 296px; height: 419px;
    background: linear-gradient(180deg, #4d8fd6 0%, #8fb8e0 45%, #6f8a4c 70%, #4f6a2e 100%);
  }
  .practice-name { top: 843px; font-size: 24px; font-weight: 700; color: var(--green); font-family: "Roboto", sans-serif; }
  .address { top: 885px; font-size: 19px; line-height: 26px; font-family: "Roboto", sans-serif; }
  .phone { top: 976px; font-size: 19px; font-family: "Roboto", sans-serif; }
  .web { top: 1014px; font-size: 18px; line-height: 25px; font-family: "Roboto", sans-serif; }
  .headline {
    top: 241px; font-weight: 700; font-size: 46px; line-height: 58px; color: var(--navy);
  }
  .headline__and { color: var(--green); }
  .mood {
    position: absolute; left: 48px; top: 455px; width: 455px; height: 455px;
  }
  .mood__photo {
    position: absolute; inset: 6px; border-radius: 50%;
    background: radial-gradient(circle at 35% 30%, #fff3c8 0%, #e9cf8a 30%, #b49a62 60%, #6d6a3c 100%);
  }
  .mood__ring { position: absolute; inset: 0; }
  .tagline {
    top: 951px; font-size: 27px; line-height: 39px; color: var(--white);
  }
</style>
</head>
<body>
  <main class="flyer">
    <section class="panel panel--contact">
      <div class="brand">
        <div class="brand__dot"></div>
        <div class="brand__name">GELASSENHEITSWERKSTATT</div>
      </div>
      <p class="centered service">SYSTEMISCHE BERATUNG &amp; COACHING</p>
      <p class="centered advisor">Dr. Helena Marcovaldi</p>
      <p class="centered credentials">Systemische Beraterin (Mitglied der VSBK)<br>Heilpraktikerin für Psychotherapie</p>
      <div class="portrait" role="img" aria-label="Foto der Beraterin an einem Wegweiser auf einem Berghang vor blauem Himmel"></div>
      <p class="centered practice-name">Gelassenheitswerkstatt</p>
      <p class="centered address">Lindenweg 12<br>Rückgebäude<br>80797 München</p>
      <p class="centered phone">0151 240 77 318</p>
      <p class="centered web">info@gelassenheitswerkstatt.de<br>www.gelassenheitswerkstatt.de</p>
    </section>
    <section class="panel panel--cover">
      <div class="brand">
        <div class="brand__dot"></div>
        <div class="brand__name">GELASSENHEITSWERKSTATT</div>
      </div>
      <h1 class="centered headline">Krisenbegleitung<br><span class="headline__and">und</span><br>Lebensberatung</h1>
      <div class="mood">
        <div class="mood__photo" role="img" aria-label="Nachdenkliche Frau sitzt im Dünengras im warmen Gegenlicht"></div>
        <svg class="mood__ring" viewBox="0 0 455 455" aria-hidden="true">
          <circle cx="227.5" cy="227.5" r="224" fill="none" stroke="#3f9f35" stroke-width="4"/>
          <circle cx="228.5" cy="226.5" r="221" fill="none" stroke="#3f9f35" stroke-width="1.5" opacity="0.7"/>
        </svg>
      </div>
      <p class="centered tagline">Psychologische Beratungspraxis<br>für Mütter, Schwangere und<br>Frauen mit Kinderwunsch</p>
    </section>
  </main>
</body>
</html>
```